Web design for software company

I'm a software developer that designs high end specialist web applications, mobile apps and user friendly applications for medium to large customers. I integrate different systems together within a company and provide web based applications or mobile apps to view and edit information in that web of linked systems.

I currently work alone, basically selling my time on specialist projects, but also build my own software solutions which I eventually want to put into the market.

My company name is Overthread (lowercase 'L' for logic) and I work from the Netherlands. I've attached my current logo which is basically just text in VOXbox font. Current colours are mustard yellow and grey, but i'm open to other options to better fit the web design.

I've got a sort of slogan: "Specialized software development" - better ideas are welcome. The slogan in the logo attachment is older.

I'm looking for a site design that reflects my work as being on the cutting edge of technology, but being clear and simple. My thinking with the name Overthread is that it refers to the underlying mechanism and logic of software.

The site will not be text heavy, so some kind of large graphic to do with software design is welcome. I expect about 4 or 5 main pages or sections of the site in which i'll eventually add things like a blog or contact info etc.

Industry/Entity Type

It Company

Number of Pages Required

1 page

Font styles to use
Sans Serif

Requirements
Nice to have
• A large graphic or photo relevant to my focus as a software developer. Something that shows connecting of software systems with perhaps a variety of devices/browsers that would display data from that cloud of systems.
• Something like these (allthough these are ugly - but the idea is what i mean):
• http://img4.pixvaultimages.example/2000517/22458/i/450/pixvault_224581133-Cloud-computing-user-interface.jpg
• http://business.tamblinet.example/images/modules/mobile-device-policy-design-banner.png
• https://www.pagecraftly.example/images/responsive-web-design.jpg
• http://www.norvexa.example/images/web_apps.png
• https://www.keyportal.example/assets/img/product/web-app@2x.png?v2
Should not have
• Photographs of smiling happy people looking at a screen that make it look like it's a huge business with many offices. I'm a one-man company which could perhaps grow a little bit, but i want to focus on my expertise instead of size.

```html
<!DOCTYPE html>
<html lang="en">
<head>
<meta charset="utf-8">
<title>Overthread — Specialized Software Development</title>
<link href="https://fonts.googleapis.com/css2?family=Raleway:wght@400;500;600;700;800&family=Open+Sans:wght@400;600;700&display=swap" rel="stylesheet">
<style>
  :root{
    --yellow:#f9d61e;
    --olive:#8a7414;
    --dark:#3a3a3a;
    --darker:#2f2f2f;
    --ink:#262626;
    --text:#555;
    --muted:#8a8a8a;
    --line:#dcdcdc;
    --panel:#f0f0f0;
    --white:#fff;
    --heading:"Raleway",sans-serif;
    --body:"Open Sans",sans-serif;
  }
  *{box-sizing:border-box;margin:0;padding:0}
  html,body{width:1200px;height:2239px;overflow:hidden;background:var(--white)}
  body{position:relative;font-family:var(--body);color:var(--text)}
  .abs{position:absolute}

  /* Header */
  .topbar{position:absolute;left:0;top:0;width:1200px;height:97px;background:var(--dark)}
  .brand{position:absolute;left:82px;top:22px}
  .brand-name{font-family:var(--heading);font-weight:800;font-size:40px;letter-spacing:1px;color:var(--yellow);line-height:44px}
  .brand-tag{font-family:var(--heading);font-size:9px;font-weight:600;color:var(--white);text-align:right;letter-spacing:.3px;margin-top:-2px}
  .contact-item{position:absolute;top:28px;display:flex;align-items:center;gap:10px;color:var(--white);font-family:var(--heading);font-size:13px;line-height:17px}
  .contact-item b{font-weight:700}
  .contact-icon{width:36px;height:36px}

  /* Nav */
  .nav{position:absolute;left:0;top:97px;width:1200px;height:48px;background:var(--yellow)}
  .nav a{position:absolute;top:16px;font-family:var(--heading);font-weight:600;font-size:15px;color:var(--ink);text-decoration:none;letter-spacing:.3px}
  .nav a.active{padding-bottom:4px;border-bottom:2px solid var(--ink)}
  .live-chat{position:absolute;left:934px;top:0;width:186px;height:48px;background:var(--olive);color:var(--white);font-family:var(--heading);font-weight:600;font-size:17px;display:flex;align-items:center;justify-content:center;gap:10px}

  /* Hero */
  .hero{position:absolute;left:0;top:145px;width:1200px;height:442px;background:radial-gradient(ellipse at 50% 55%,#1a1a1a 0%,#050505 70%)}
  .hero-title{position:absolute;left:0;top:86px;width:1200px;text-align:center;font-family:var(--heading);font-weight:700;font-size:36px;line-height:50px;color:var(--white);letter-spacing:.5px}

  /* Welcome */
  .welcome{position:absolute;left:0;top:587px;width:1200px;height:525px;background:var(--white)}
  .section-heading{font-family:var(--heading);font-weight:700;color:var(--ink);letter-spacing:.3px}
  .section-heading span{color:var(--yellow)}
  .rule{position:absolute;height:2px;background:var(--line)}
  .rule::before{content:"";position:absolute;left:0;top:0;height:2px;width:46px;background:var(--ink)}
  .welcome h1{position:absolute;left:82px;top:50px;font-size:31px}
  .welcome h2{position:absolute;left:82px;top:128px;font-family:var(--body);font-weight:600;font-size:17px;color:var(--ink)}
  .welcome p{position:absolute;left:82px;top:164px;width:508px;font-size:14px;line-height:27px;color:var(--text);text-align:justify;letter-spacing:.2px}
  .btn{position:absolute;height:35px;background:var(--yellow);display:flex;align-items:center;justify-content:space-between;padding:0 10px 0 12px;font-family:var(--heading);font-weight:700;font-size:13px;color:var(--ink);border-radius:2px}
  .btn svg{width:20px;height:20px}

  .features{position:absolute;left:649px;top:0;width:551px;height:525px}
  .feature{position:absolute;border-left:2px solid #ececec;border-bottom:2px solid #ececec;text-align:center}
  .feature svg{position:absolute;left:50%;top:55px;width:98px;height:98px;margin-left:-49px}
  .feature .label{position:absolute;left:0;right:0;top:186px;font-family:var(--heading);font-weight:600;font-size:14px;line-height:20px;color:var(--ink)}

  /* Services */
  .services{position:absolute;left:0;top:1112px;width:1200px;height:455px;background:var(--panel)}
  .services h2{position:absolute;left:0;width:1200px;top:44px;text-align:center;font-size:31px}
  .services .center-rule{position:absolute;left:509px;top:104px;width:182px;height:1px;background:#d6d6d6}
  .services .center-rule::after{content:"";position:absolute;left:69px;top:-1px;width:44px;height:3px;background:var(--ink)}
  .service{position:absolute;top:152px;width:360px;text-align:center}
  .service svg{width:104px;height:104px;display:block;margin:0 auto}
  .service h3{margin-top:40px;font-family:var(--heading);font-weight:600;font-size:23px;color:var(--ink)}
  .service p{margin-top:12px;font-family:var(--heading);font-weight:600;font-size:14px;line-height:22px;color:var(--ink)}

  /* Lower columns */
  .lower{position:absolute;left:0;top:1567px;width:1200px;height:527px;background:var(--white)}
  .col-heading{position:absolute;top:50px;font-size:25px}
  .solutions-image{position:absolute;left:82px;top:115px;width:330px;height:160px;background:linear-gradient(120deg,#0d2a48 0%,#1f6fa8 45%,#3fb0e6 75%,#0b3a63 100%)}
  .col-text{position:absolute;font-size:13px;line-height:25px;color:var(--text);letter-spacing:.2px}
  .post{position:absolute;left:440px;width:340px;height:92px}
  .post .thumb{position:absolute;left:0;top:0;width:93px;height:88px}
  .post h4{position:absolute;left:112px;top:-2px;font-family:var(--heading);font-weight:700;font-size:14px;color:var(--ink)}
  .post .date{position:absolute;left:112px;top:24px;font-family:var(--heading);font-weight:700;font-size:11px;color:var(--ink)}
  .post .excerpt{position:absolute;left:112px;top:46px;width:222px;font-size:12px;line-height:20px;color:var(--muted)}
  .post .excerpt em{font-style:normal;color:var(--yellow)}
  .field{position:absolute;left:803px;width:318px;height:31px;border:1px solid #d4d4d4;border-radius:3px;background:var(--white)}

  /* Footer */
  .footer{position:absolute;left:0;top:2094px;width:1200px;height:145px;background:var(--dark)}
  .footer-box{position:absolute;top:19px;height:75px;border:1px solid #6a6a6a;background:#454545;padding:6px 10px}
  .footer-box h5{font-family:var(--heading);font-weight:600;font-size:14px;color:var(--white)}
  .footer-box .input{position:absolute;left:10px;top:39px;width:172px;height:26px;background:var(--white);border-radius:2px;font-size:10px;color:var(--ink);padding:6px 8px}
  .footer-box .go{position:absolute;left:189px;top:39px;width:30px;height:26px;background:var(--white)}
  .footer-box .line{display:flex;align-items:center;gap:8px;font-size:10px;color:var(--white);margin-top:6px}
  .social{position:absolute;top:38px;width:24px;height:24px;background:#6d6d6d;border-radius:2px}
  .footer-brand{position:absolute;left:881px;top:43px;width:241px;text-align:right;font-family:var(--heading);font-weight:800;font-size:30px;letter-spacing:1px;color:#b5b5b5}
  .copyright{position:absolute;left:881px;top:96px;width:216px;text-align:center;font-family:var(--heading);font-weight:600;font-size:11px;line-height:16px;color:var(--white)}
  .footer-nav a{position:absolute;top:113px;font-family:var(--heading);font-weight:600;font-size:12px;color:var(--white);text-decoration:none}
  .footer-nav a.active{color:var(--yellow)}
</style>
</head>
<body>

<header class="topbar">
  <div class="brand">
    <div class="brand-name">OVERTHREAD</div>
    <div class="brand-tag">CUSTOM SOFTWARE SOLUTIONS</div>
  </div>
  <div class="contact-item" style="left:762px">
    <svg class="contact-icon" viewBox="0 0 36 36"><circle cx="18" cy="18" r="16" fill="none" stroke="#f9d61e" stroke-width="2"/><path d="M13 11c1-1 2 0 3 2s0 2-1 3c1 2 3 4 5 5 1-1 1-2 3-1s3 2 2 3c-1 2-3 3-5 2-4-2-7-5-8-9-1-2 0-4 1-5z" fill="#f9d61e"/></svg>
    <div>Call Us<br><b>(123)-456-7890</b></div>
  </div>
  <div class="contact-item" style="left:930px">
    <svg class="contact-icon" viewBox="0 0 36 36"><circle cx="18" cy="18" r="16" fill="none" stroke="#f9d61e" stroke-width="2"/><rect x="10" y="12" width="16" height="12" rx="1" fill="#f9d61e"/><path d="M10 13l8 6 8-6" fill="none" stroke="#3a3a3a" stroke-width="1.5"/></svg>
    <div>Email Us<br><b>info@overthread.com</b></div>
  </div>
</header>

<nav class="nav">
  <a class="active" href="#" style="left:82px">HOME</a>
  <a href="#" style="left:191px">ABOUT ME</a>
  <a href="#" style="left:337px">SERVICES</a>
  <a href="#" style="left:478px">SOFTWARE SOLUTIONS</a>
  <a href="#" style="left:722px">CONTACT US</a>
  <div class="live-chat">
    <svg width="14" height="16" viewBox="0 0 14 16"><circle cx="7" cy="4.5" r="4" fill="#fff"/><path d="M0 16c0-5 3-7 7-7s7 2 7 7z" fill="#fff"/></svg>
    Live Chat
  </div>
</nav>

<section class="hero" role="img" aria-label="Flat illustration of a software developer's desk seen from above: monitor with code, keyboard, wireframe sketches, calculator, magnifier and coffee cup">
  <div class="hero-title">SPECIALIZED<br>SOFTWARE DEVELOPMENT</div>
</section>

<section class="welcome">
  <h1 class="section-heading">WELCOME TO <span>OVERTHREAD</span></h1>
  <div class="rule" style="left:82px;top:106px;width:493px"></div>
  <h2>Lorem ipsum dolor sit amet, consectetuer in the adipiscing</h2>
  <p>Lorem ipsum dolor sit amet, consectetuer adipiscing elit, sed diam nonummy nibh euismod tincidunt ut laoreet dolore magna aliquam erat volutpat. Ut wisi enim ad minim veniam, quis nostrud exercisei tation ullamcorper suscipit lobortis nisl ut aliquip ex ea commodo consequat. Duis autem vel eumorl iriure dolor in hendrerit in vulputate velLorem ipsum dolor sit amet, consectetuer adipiscing elit, sed diam nonummy nibh euismod tincidunt ut laoreet dolore magna aliquam erat volutpat. Ut nibh euismod tincidunt ut laoreet dolore magna aliquam erat volutpat. Ut wisi enim ad minim veniam, quis nostrud exercisei</p>
  <div class="btn" style="left:82px;top:443px;width:136px">READ MORE
    <svg viewBox="0 0 20 20"><circle cx="10" cy="10" r="9" fill="#fff"/><path d="M8 6l4 4-4 4" fill="none" stroke="#262626" stroke-width="1.8"/></svg>
  </div>

  <div class="features">
    <div class="feature" style="left:0;top:0;width:258px;height:261px">
      <svg viewBox="0 0 98 98"><circle cx="49" cy="49" r="49" fill="#333"/><path d="M49 0a49 49 0 0 0 0 98z" fill="#f9d61e"/><path d="M26 46l10-8h10l6 4 8-4h12l-12 16-8 8-6-4-6 2z" fill="#fff"/></svg>
      <div class="label">CUSTOM SOFTWARE &amp;<br>CONSULTING</div>
    </div>
    <div class="feature" style="left:258px;top:0;width:293px;height:261px">
      <svg viewBox="0 0 98 98"><circle cx="49" cy="49" r="49" fill="#333"/><rect x="27" y="31" width="38" height="30" fill="none" stroke="#fff" stroke-width="3"/><rect x="32" y="36" width="12" height="20" fill="#fff"/><circle cx="66" cy="62" r="7" fill="#fff"/><circle cx="66" cy="62" r="3" fill="#333"/></svg>
      <div class="label">MODERN, USER FRIENDLY<br>SOFTWARE</div>
    </div>
    <div class="feature" style="left:0;top:261px;width:258px;height:264px">
      <svg viewBox="0 0 98 98"><circle cx="49" cy="49" r="49" fill="#333"/><circle cx="44" cy="50" r="14" fill="none" stroke="#fff" stroke-width="6" stroke-dasharray="6 4"/><circle cx="44" cy="50" r="6" fill="#fff"/><path d="M54 56l16-20 5 4-16 20-7 2z" fill="#fff"/></svg>
      <div class="label">CUTTING EDGE SOFTWARE<br>CUSTOM DESIGNED</div>
    </div>
    <div class="feature" style="left:258px;top:261px;width:293px;height:264px">
      <svg viewBox="0 0 98 98"><circle cx="49" cy="49" r="49" fill="#333"/><rect x="26" y="38" width="40" height="28" fill="none" stroke="#fff" stroke-width="3"/><rect x="40" y="66" width="12" height="6" fill="#fff"/><rect x="34" y="72" width="24" height="3" fill="#fff"/><circle cx="64" cy="34" r="8" fill="none" stroke="#fff" stroke-width="3" stroke-dasharray="4 2"/><circle cx="74" cy="46" r="5" fill="none" stroke="#fff" stroke-width="2.5"/></svg>
      <div class="label">HIGH END WEB AND<br>MOBILE APPLICATIONS</div>
    </div>
  </div>
</section>

<section class="services">
  <h2 class="section-heading">MY SERVICES</h2>
  <div class="center-rule"></div>
  <div class="service" style="left:48px">
    <svg viewBox="0 0 104 104"><circle cx="52" cy="52" r="50" fill="none" stroke="#262626" stroke-width="2.5"/><rect x="30" y="34" width="44" height="30" rx="2" fill="none" stroke="#262626" stroke-width="3"/><rect x="46" y="64" width="12" height="6" fill="#262626"/><rect x="40" y="70" width="24" height="3" fill="#262626"/><path d="M40 58l22-20 3 3-22 20z" fill="#262626"/></svg>
    <h3>Web Applications</h3>
    <p>Lorem ipsum dolor sit amet,<br>consectetuer adipiscing elit sed<br>diamsit almet dolor</p>
  </div>
  <div class="service" style="left:404px">
    <svg viewBox="0 0 104 104"><circle cx="52" cy="52" r="50" fill="#f9d61e" stroke="#262626" stroke-width="2.5"/><rect x="38" y="26" width="28" height="52" rx="4" fill="none" stroke="#262626" stroke-width="3"/><circle cx="52" cy="52" r="9" fill="none" stroke="#262626" stroke-width="5" stroke-dasharray="4 3"/><circle cx="52" cy="52" r="3" fill="#262626"/><circle cx="52" cy="72" r="2" fill="#262626"/></svg>
    <h3>Mobile Apps</h3>
    <p>Lorem ipsum dolor sit amet,<br>consectetuer adipiscing elit sed<br>diamsit almet dolor</p>
  </div>
  <div class="service" style="left:756px">
    <svg viewBox="0 0 104 104"><circle cx="52" cy="52" r="50" fill="none" stroke="#262626" stroke-width="2.5"/><path d="M28 52h12l4 8h16l4-8h12v20H28z" fill="#262626"/><path d="M40 50c2-10 10-16 22-16v-8l12 12-12 12v-8c-8 0-14 2-22 8z" fill="#262626"/></svg>
    <h3>User Friendly Applications</h3>
    <p>Lorem ipsum dolor sit amet,<br>consectetuer adipiscing elit sed<br>diamsit almet dolor</p>
  </div>
</section>

<section class="lower">
  <h2 class="section-heading col-heading" style="left:82px">SOFTWARE <span>SOLUTIONS</span></h2>
  <div class="rule" style="left:82px;top:96px;width:330px"></div>
  <div class="solutions-image" role="img" aria-label="Photo of hands holding a tablet with a glowing cloud network of connected devices above it"></div>
  <p class="col-text" style="left:82px;top:300px;width:330px">Lorem ipsum dolor sit amet, dolor sit consectetuer adipiscing elit, sed sit diam nonummy nibh euismod almet tincidunt ut laoreet dolore magna al aliquam erat volutpat. Ut wisi enim ad minim veniam, quis nostrud dolor exercisei tation ullamcorper.</p>
  <div class="btn" style="left:82px;top:440px;width:136px">GET STARTED
    <svg viewBox="0 0 20 20"><circle cx="10" cy="10" r="9" fill="#fff"/><path d="M8 6l4 4-4 4" fill="none" stroke="#262626" stroke-width="1.8"/></svg>
  </div>

  <h2 class="section-heading col-heading" style="left:440px">BLOG <span>POSTS</span></h2>
  <div class="rule" style="left:440px;top:96px;width:330px"></div>
  <article class="post" style="top:117px">
    <div class="thumb" role="img" aria-label="Photo of a person working on a laptop" style="background:linear-gradient(135deg,#2b4a63,#6b8ba3)"></div>
    <h4>UT TELLUS DOLOR DAPIBUS</h4>
    <div class="date">06.JULY.2016</div>
    <div class="excerpt">Duis autem vel eum iriure dolor opl vulputate velitm essemol ... <em>[+]</em></div>
  </article>
  <article class="post" style="top:221px">
    <div class="thumb" role="img" aria-label="Photo of a hand touching a tablet showing charts" style="background:linear-gradient(135deg,#b9cfe0,#6f97b8)"></div>
    <h4>UT TELLUS DOLOR DAPIBUS</h4>
    <div class="date">05.JULY.2016</div>
    <div class="excerpt">Duis autem vel eum iriure dolor opl vulputate velitm essemol ... <em>[+]</em></div>
  </article>
  <article class="post" style="top:326px">
    <div class="thumb" role="img" aria-label="Photo of a person with a digital interface" style="background:linear-gradient(135deg,#cfe7f5,#5aa6d6)"></div>
    <h4>UT TELLUS DOLOR DAPIBUS</h4>
    <div class="date">05.JULY.2016</div>
    <div class="excerpt">Duis autem vel eum iriure dolor opl vulputate velitm essemol ... <em>[+]</em></div>
  </article>
  <div class="btn" style="left:440px;top:440px;width:136px">READ MORE
    <svg viewBox="0 0 20 20"><circle cx="10" cy="10" r="9" fill="#fff"/><path d="M8 6l4 4-4 4" fill="none" stroke="#262626" stroke-width="1.8"/></svg>
  </div>

  <h2 class="section-heading col-heading" style="left:803px">QUICK <span>INQUIRY</span></h2>
  <div class="rule" style="left:803px;top:96px;width:331px"></div>
  <p class="col-text" style="left:803px;top:112px;width:330px;font-size:13px;line-height:25px">Lorem ipsum dolor sit amet, dolor sit consectetuer adipiscing elit, sed sit diam nonummy nibh eu amet, dolor sit conse</p>
  <div class="field" style="top:212px"></div>
  <div class="field" style="top:252px"></div>
  <div class="field" style="top:293px"></div>
  <div class="field" style="top:334px;height:80px"></div>
  <div class="btn" style="left:803px;top:440px;width:109px">SUBMIT
    <svg viewBox="0 0 20 20"><circle cx="10" cy="10" r="9" fill="#fff"/><path d="M8 6l4 4-4 4" fill="none" stroke="#262626" stroke-width="1.8"/></svg>
  </div>
</section>

<footer class="footer">
  <div class="footer-box" style="left:82px;width:233px">
    <h5>Subscribe to Newsletter</h5>
    <div class="input">Email here</div>
    <svg class="go" viewBox="0 0 30 26"><rect width="30" height="26" fill="#fff"/><path d="M12 7l6 6-6 6" fill="none" stroke="#262626" stroke-width="2.5"/></svg>
  </div>
  <div class="footer-box" style="left:351px;width:179px">
    <h5>Contact Us</h5>
    <div class="line"><svg width="11" height="11" viewBox="0 0 11 11"><path d="M2 1c1-1 2 0 2 1s0 1-1 2c1 1 2 2 3 3 1-1 1-1 2-1s2 1 1 2c-1 2-3 2-5 0S0 4 2 1z" fill="#f9d61e"/></svg>012-345-6789</div>
    <div class="line" style="margin-top:3px"><svg width="11" height="9" viewBox="0 0 11 9"><rect width="11" height="9" fill="#f9d61e"/><path d="M0 1l5.5 4L11 1" fill="none" stroke="#454545"/></svg>info@overthread.com</div>
  </div>
  <div class="footer-box" style="left:567px;width:112px">
    <h5>Follow Us</h5>
    <div class="social" style="left:10px"></div>
    <div class="social" style="left:44px"></div>
    <div class="social" style="left:78px"></div>
  </div>
  <div class="footer-brand">OVERTHREAD</div>
  <div class="copyright">COPYRIGHT © 2016 OVERTHREAD.<br>ALL RIGHTS RESERVED.</div>
  <nav class="footer-nav">
    <a class="active" href="#" style="left:82px">HOME</a>
    <a href="#" style="left:158px">ABOUT ME</a>
    <a href="#" style="left:264px">SERVICES</a>
    <a href="#" style="left:366px">SOFTWARE SOLUTIONS</a>
    <a href="#" style="left:551px">CONTACT US</a>
  </nav>
</footer>

</body>
</html>
```